Electrical Engineering Business Card Design

I need a business card design for an engineering consulting company based in Orlando, FL. I have had a logo created which the files are attached. We work primarily in the theme park and entertainment market sector but do projects in all market sectors. We have been serving Central Florida since 1994 and continue to strive to serve our clients and provide outstanding designs.
Theme Park

```html
<!DOCTYPE html>
<html lang="en">
<head>
<meta charset="utf-8">
<title>Voltline Partners, PA – Business Card</title>
<link href="https://fonts.googleapis.com/css2?family=Source+Sans+3:wght@400;600;700&display=swap" rel="stylesheet">
<style>
  :root {
    --stage: #d3d3d3;
    --lime: #8dc63f;
    --ink: #0a0a0a;
    --paper: #ffffff;
    --body-text: #555555;
  }
  html, body {
    margin: 0;
    width: 1200px;
    height: 938px;
    overflow: hidden;
    background: var(--stage);
    font-family: "Source Sans 3", sans-serif;
  }
  .card {
    position: absolute;
    left: 230px;
    width: 742px;
    box-shadow: 0 4px 14px rgba(0,0,0,0.35);
  }
  .card--front {
    top: 26px;
    height: 421px;
    background: var(--lime);
  }
  .card--back {
    top: 484px;
    height: 423px;
    background: var(--paper);
  }
  .brand-mark {
    position: absolute;
    background: var(--ink);
  }
  .card--front .brand-mark {
    left: 311px;
    top: 96px;
    width: 120px;
    height: 120px;
  }
  .brand-name {
    position: absolute;
    margin: 0;
    font-weight: 700;
    white-space: nowrap;
    color: var(--ink);
  }
  .card--front .brand-name {
    left: 0;
    width: 100%;
    top: 258px;
    text-align: center;
    font-size: 54px;
    line-height: 1;
  }
  .card--back .brand-mark {
    left: 140px;
    top: 150px;
    width: 90px;
    height: 90px;
    background: var(--lime);
  }
  .card--back .brand-name {
    left: 21px;
    width: 328px;
    top: 249px;
    text-align: center;
    font-size: 29px;
    line-height: 1;
    color: #1a1a1a;
  }
  .divider {
    position: absolute;
    left: 369px;
    top: 131px;
    width: 1px;
    height: 182px;
    background: linear-gradient(to bottom, rgba(0,0,0,0), #333 50%, rgba(0,0,0,0));
  }
  .contact {
    position: absolute;
    left: 390px;
    top: 0;
  }
  .person-name {
    position: absolute;
    top: 99px;
    margin: 0;
    white-space: nowrap;
    font-size: 27px;
    font-weight: 700;
    color: var(--lime);
    line-height: 1;
  }
  .line {
    position: absolute;
    margin: 0;
    white-space: nowrap;
    font-size: 19px;
    line-height: 1;
    color: var(--body-text);
  }
  .person-title { top: 130px; left: 1px; }
  .addr-1 { top: 171px; left: 1px; }
  .addr-2 { top: 196px; left: 1px; }
  .with-icon { left: 24px; }
  .phone { top: 238px; }
  .fax { top: 268px; }
  .email { top: 298px; }
  .web { top: 324px; }
  .icon {
    position: absolute;
    left: 9px;
    width: 12px;
    height: 12px;
    fill: var(--lime);
  }
  .icon-phone { top: 242px; }
  .icon-fax { top: 272px; }
  .icon-email { top: 303px; }
  .icon-web { top: 328px; }
</style>
</head>
<body>
  <section class="card card--front">
    <div class="brand-mark"></div>
    <h1 class="brand-name">Voltline Partners, PA</h1>
  </section>

  <section class="card card--back">
    <div class="brand-mark"></div>
    <h2 class="brand-name">Voltline Partners, PA</h2>
    <div class="divider"></div>

    <div class="contact">
      <p class="person-name">Daniel Hartley, PE</p>
      <p class="line person-title">Principal</p>
      <p class="line addr-1">PO Box 480217</p>
      <p class="line addr-2">Orlando, FL 32819</p>

      <svg class="icon icon-phone" viewBox="0 0 12 12"><path d="M2.5 0.5l2 2.5-1 1.2c.6 1.5 1.8 2.7 3.3 3.3l1.2-1 2.5 2-1 2C5.5 10.5 1.5 6.5 0.5 1.5z"/></svg>
      <p class="line with-icon phone">407-555-0142</p>

      <svg class="icon icon-fax" viewBox="0 0 12 12"><rect x="3" y="0.5" width="6" height="3"/><rect x="0.5" y="4" width="11" height="5" rx="1"/><rect x="3" y="8" width="6" height="3.5"/></svg>
      <p class="line with-icon fax">407-555-0187</p>

      <svg class="icon icon-email" viewBox="0 0 12 12"><rect x="0.5" y="2" width="11" height="8"/><path d="M0.5 2l5.5 4.5 5.5-4.5" fill="none" stroke="#fff" stroke-width="1.2"/></svg>
      <p class="line with-icon email">dhartley@voltline-partners.com</p>

      <svg class="icon icon-web" viewBox="0 0 12 12"><circle cx="6" cy="6" r="5.5"/><path d="M0.5 6h11M6 0.5v11M2 3h8M2 9h8" stroke="#fff" stroke-width="0.9" fill="none"/><ellipse cx="6" cy="6" rx="2.5" ry="5.5" fill="none" stroke="#fff" stroke-width="0.9"/></svg>
      <p class="line with-icon web">www.voltline-partners.com</p>
    </div>
  </section>
</body>
</html>
```